website design for an energy technology company

Marlow Vektor Holdings is an African based company with interests in renewable energy, clean thermal power and building automation with an overall objective to ensure access to affordable, reliable, sustainable and modern energy for all.
The portal should be simple to navigate. Key attribute is to have scalable pictures of completed projects across the three different portfolios of Renewable energy, thermal power and building automation plus counters on megawatts of electricity.

Target Market(s)

Renewable energy, thermal power, building automation, smart building technology

Industry/Entity Type

Technology Equipment

Coding

Coded - Design and coding required

Number of Pages Required

5+ page

Font styles to use
Sans Serif

Colors
33a6d7
abd037
82c8e6
0255a3
33b8a4

Requirements
Must have
• Photos with human models must feature African males and females at the forefront.
We need counters on the first page and these should be represent installed base for (1) renewables-KW, (2) thermal - (kW), (3) carbon footprint saved
Nice to have
• Would like to have design that is as simple as www.qorbintel.com. With this the left hand roulette style texts will include:
Renewables - This page will now have sub menus on:
Residential Solar
Commercial building solar
Solar Rural Electrification
Windmill
Sustainable technologies

Thermal - will have sub menus like below:
Plant Operation and maintenance
Captive Power Installation

Building Automation - will have sub-menus like:
Commercial building automation
Residential Building Automation
Products
Commercial packages
Services

SDG7 News (connected to the Tz Sustainable development goals)
Blogs
In The News
Should not have
• snow, nuclear power

```html
<!DOCTYPE html>
<html lang="en">
<head>
<meta charset="utf-8">
<title>Marlow Vektor – Thermal Energy</title>
<link href="https://fonts.googleapis.com/css2?family=Raleway:wght@400;500;600;700;800&display=swap" rel="stylesheet">
<style>
  :root{
    --blue:#33a6d7;
    --green:#abd037;
    --ink:#333333;
    --muted:#6b6b6b;
    --footer:#232425;
    --footer-text:#e6e6e6;
    --white:#ffffff;
  }
  *{margin:0;padding:0;box-sizing:border-box;}
  html,body{width:886px;height:1200px;overflow:hidden;background:var(--white);}
  body{position:relative;font-family:"Raleway",sans-serif;color:var(--ink);}

  .top-bar{position:absolute;top:0;left:0;width:886px;height:2px;display:flex;}
  .top-bar span{flex:1;}
  .top-bar .b{background:var(--blue);}
  .top-bar .g{background:var(--green);}

  .site-header{position:absolute;top:2px;left:0;width:886px;height:41px;}
  .brand{position:absolute;left:69px;top:13px;display:flex;align-items:center;gap:4px;font-size:12px;font-weight:700;color:var(--blue);letter-spacing:.2px;}
  .brand i{display:block;width:8px;height:8px;border-radius:50%;background:var(--green);}
  .main-nav{position:absolute;top:18px;left:0;font-size:8.3px;font-weight:500;color:var(--ink);}
  .main-nav a{position:absolute;white-space:nowrap;color:inherit;text-decoration:none;}
  .nav-sep{position:absolute;left:739px;top:16px;width:1px;height:11px;background:#cfcfcf;}
  .nav-phone{color:var(--blue)!important;font-weight:600;}

  .hero{position:absolute;top:43px;left:0;width:886px;height:262px;
    background:linear-gradient(180deg,#3b2c3a 0%,#5d3a3a 35%,#8a5a33 60%,#3a2a24 100%);}
  .hero-title{position:absolute;top:147px;left:0;width:886px;text-align:center;font-size:41px;font-weight:800;color:var(--white);letter-spacing:-.5px;}
  .hero-title em{font-style:normal;color:var(--green);}

  .project{position:absolute;width:181px;}
  .project .photo{width:181px;height:116px;}
  .project h3{margin-top:4px;font-size:14.4px;font-weight:500;color:var(--ink);margin-left:-1px;}
  .project p{margin-top:3px;font-size:8.9px;line-height:14px;color:var(--muted);}

  .site-footer{position:absolute;top:951px;left:0;width:886px;height:249px;
    background:radial-gradient(ellipse at 50% 40%,#3a3b3c 0%,var(--footer) 70%);color:var(--footer-text);}
  .f-col{position:absolute;top:26px;}
  .f-col h4{font-size:14.4px;font-weight:500;color:var(--green);margin-bottom:10px;}
  .links li{list-style:none;font-size:8.3px;height:19.4px;}
  .svc strong{display:block;font-size:9px;font-weight:700;margin-bottom:3px;}
  .svc small{display:block;font-size:7px;line-height:12.7px;color:#bdbdbd;}
  .svc hr{border:0;border-top:1px solid #4a4a4a;width:117px;margin:7px 0 8px;}
  .contact-row{position:relative;padding-left:12px;font-size:8.3px;line-height:12px;}
  .contact-row svg{position:absolute;left:0;top:2px;}
  .socials{display:flex;gap:5px;margin-top:17px;}
  .socials span{width:16px;height:16px;border-radius:50%;background:var(--white);}
  .form-field{position:absolute;background:var(--white);font-size:7.2px;color:#8a8a8a;padding:7px 6px;}
  .send{position:absolute;left:761px;top:150px;width:56px;height:21px;background:var(--blue);color:var(--white);font-size:7.8px;font-weight:700;display:flex;align-items:center;justify-content:center;}
  .copyright{position:absolute;top:209px;left:0;width:886px;text-align:center;font-size:7.8px;color:#9a9a9a;font-weight:500;}
  .copyright b{color:var(--blue);font-weight:700;}
</style>
</head>
<body>
  <div class="top-bar"><span class="b"></span><span class="g"></span></div>

  <header class="site-header">
    <div class="brand"><i></i>MARLOW VEKTOR</div>
    <nav class="main-nav">
      <a style="left:487px">HOME</a>
      <a style="left:543px">SERVICES</a>
      <a style="left:614px">PRODUCTS</a>
      <a style="left:690px">ABOUT US</a>
      <a class="nav-phone" style="left:746px">+2 (555) 246 7390</a>
    </nav>
    <div class="nav-sep"></div>
  </header>

  <section class="hero" role="img" aria-label="Thermal power plant with chimneys at dusk">
    <h1 class="hero-title"><em>THERMAL</em> ENERGY</h1>
  </section>

  <main>
    <article class="project" style="left:69px;top:355px"><div class="photo" role="img" aria-label="Power plant on the coast at dusk" style="background:linear-gradient(180deg,#7f8fa6,#4a5160 60%,#8a6a4a)"></div><h3>Finibus Bonorum</h3><p>Sed ut perspiciatis unde omnis iste natus error sit voluptatem</p></article>
    <article class="project" style="left:258px;top:355px"><div class="photo" role="img" aria-label="Cooling towers releasing steam" style="background:linear-gradient(180deg,#e6ecef,#b9c0c4 70%,#6e7a52)"></div><h3>Finibus Bonorum</h3><p>Sed ut perspiciatis unde omnis iste natus error sit voluptatem</p></article>
    <article class="project" style="left:447px;top:355px"><div class="photo" role="img" aria-label="Engineer checking a control panel" style="background:linear-gradient(135deg,#1f3b4d,#5f7f8f 55%,#223444)"></div><h3>Finibus Bonorum</h3><p>Sed ut perspiciatis unde omnis iste natus error sit voluptatem</p></article>
    <article class="project" style="left:636px;top:355px"><div class="photo" role="img" aria-label="Worker in a red hard hat overlooking a plant hall" style="background:linear-gradient(135deg,#8aa1a8,#3a3d40 55%,#6f8a88)"></div><h3>Finibus Bonorum</h3><p>Sed ut perspiciatis unde omnis iste natus error sit voluptatem</p></article>

    <article class="project" style="left:69px;top:549px"><div class="photo" role="img" aria-label="Two engineers among steel pipework" style="background:linear-gradient(135deg,#9fb3c4,#3456a3 60%,#c5ccd2)"></div><h3>Finibus Bonorum</h3><p>Sed ut perspiciatis unde omnis iste natus error sit voluptatem</p></article>
    <article class="project" style="left:258px;top:549px"><div class="photo" role="img" aria-label="Technician servicing a turbine" style="background:linear-gradient(135deg,#8e959b,#c9cdd0 45%,#d86b2c)"></div><h3>Finibus Bonorum</h3><p>Sed ut perspiciatis unde omnis iste natus error sit voluptatem</p></article>
    <article class="project" style="left:447px;top:549px"><div class="photo" role="img" aria-label="Plant corridor with yellow railings" style="background:linear-gradient(135deg,#5a5f63,#9ba0a3 50%,#c8a23a)"></div><h3>Finibus Bonorum</h3><p>Sed ut perspiciatis unde omnis iste natus error sit voluptatem</p></article>
    <article class="project" style="left:636px;top:549px"><div class="photo" role="img" aria-label="Two workers inspecting a steel structure" style="background:linear-gradient(135deg,#c4ccd3,#3059a8 55%,#8d9aa5)"></div><h3>Finibus Bonorum</h3><p>Sed ut perspiciatis unde omnis iste natus error sit voluptatem</p></article>

    <article class="project" style="left:69px;top:739px"><div class="photo" role="img" aria-label="Row of blue pumps in a pump room" style="background:linear-gradient(180deg,#8c9093,#5a6570 45%,#2c5aa8)"></div><h3>Finibus Bonorum</h3><p>Sed ut perspiciatis unde omnis iste natus error sit voluptatem</p></article>
    <article class="project" style="left:258px;top:739px"><div class="photo" role="img" aria-label="Worker in blue overalls at a refinery" style="background:linear-gradient(135deg,#d8dde0,#9aa3a8 45%,#2c55a5)"></div><h3>Finibus Bonorum</h3><p>Sed ut perspiciatis unde omnis iste natus error sit voluptatem</p></article>
  </main>

  <footer class="site-footer">
    <div class="f-col" style="left:69px">
      <h4>Quick Links</h4>
      <ul class="links"><li>Home</li><li>About Us</li><li>Services</li><li>Products</li><li>Contact Us</li></ul>
    </div>
    <div class="f-col svc" style="left:227px">
      <h4>Services</h4>
      <strong>Renewable Energy</strong>
      <small>Industrial and residential solar</small>
      <small>Large and small wind turbines</small>
      <hr>
      <strong>Building Automation</strong>
      <small>Commercial</small>
      <small>Residential</small>
    </div>
    <div class="f-col" style="left:410px">
      <h4>Contact Us</h4>
      <div class="contact-row"><svg width="7" height="9" viewBox="0 0 7 9"><path d="M3.5 0A3.3 3.3 0 0 0 .2 3.3C.2 5.8 3.5 9 3.5 9s3.3-3.2 3.3-5.7A3.3 3.3 0 0 0 3.5 0z" fill="#33a6d7"/><circle cx="3.5" cy="3.3" r="1.2" fill="#232425"/></svg>27c Kestrel Row, Harlan Park<br>Dunmore 4100</div>
      <div class="contact-row" style="margin-top:17px"><svg width="7" height="9" viewBox="0 0 7 9"><path d="M1.2 0h1.6l.6 2.2-1 .8c.4 1.4 1 2.4 2 3.2l.9-.7 1.7 1.1-.6 2.2C3 8.6.2 5 .5.8z" fill="#33a6d7"/></svg>+2 (555) 246 7390</div>
      <div class="contact-row" style="margin-top:16px"><svg width="9" height="7" viewBox="0 0 9 7"><rect width="9" height="7" fill="#33a6d7"/><path d="M0 0l4.5 3.8L9 0" stroke="#232425" stroke-width=".8" fill="none"/></svg>info@marlowvektor.com</div>
      <div class="socials"><span></span><span></span><span></span></div>
    </div>
    <div class="f-col" style="left:604px">
      <h4>Reach Us</h4>
    </div>
    <div class="form-field" style="left:604px;top:54px;width:170px;height:21px">Name:</div>
    <div class="form-field" style="left:604px;top:78px;width:170px;height:21px">Email:</div>
    <div class="form-field" style="left:604px;top:102px;width:213px;height:43px">Message:</div>
    <div class="send">SEND</div>
    <p class="copyright">COPYRIGHT © 2020 <b>MARLOW VEKTOR</b>. ALL RIGHTS RESERVED.</p>
  </footer>
</body>
</html>
```